Sports medicine multidisciplinary brochures

Multi-disciplinary sports medicine clinic. Need a range of pamphlet / foldable brochures to advertise our various services. Looking at keeping a similar 'look' between the various brochures to still ID as being part of the group, but perhaps slight colour variation / different front pic to distinguish them. Looking at a pamphlet for: 1) General clinic (about us) info 2) Concussion info 3) Podiatry 4) Sports Physicians 5) Exercise Physiology 6) Osteoarthritis 7) Physiotherapy. Modern feel, but still warm / inviting. See attached logo / cards / etc. Thank you!

Target Market(s)

Athletes, sports injuries + general health / medical

Industry/Entity Type

Clinic

Requirements
Nice to have
• Simple, warm design. Activity / health / lifestyle related feel.
• Design to allow easy adaptation of wording / content.

```html
<!DOCTYPE html>
<html lang="en">
<head>
<meta charset="utf-8">
<title>Kinetra brochure pages</title>
<link rel="stylesheet" href="https://fonts.googleapis.com/css2?family=Mulish:wght@400;500;800&display=swap">
<style>
  :root {
    --backdrop: #d6d6d6;
    --paper: #ffffff;
    --ink: #3a3a3a;
    --accent: #e8610f;
    --orange-deep: #e8670f;
    --orange-light: #f3960a;
    --brand-green: #2e8b4e;
    --mint: #c6e6d4;
    --shadow: rgba(0,0,0,0.28);
  }
  * { box-sizing: border-box; margin: 0; padding: 0; }
  html, body { width: 1200px; height: 1200px; overflow: hidden; }
  body {
    background: var(--backdrop);
    font-family: "Mulish", Arial, sans-serif;
    color: var(--ink);
    position: relative;
  }
  .page {
    position: absolute;
    background: var(--paper);
    box-shadow: 1px 2px 4px var(--shadow);
    overflow: hidden;
  }
  .page--front { left: 18px; top: 62px; width: 580px; height: 820px; }
  .page--back  { left: 614px; top: 278px; width: 567px; height: 802px; }

  .wave-art { position: absolute; left: 0; top: 0; width: 580px; height: 820px; }

  .brand {
    position: absolute;
    display: flex;
    align-items: center;
    gap: 8px;
    white-space: nowrap;
  }
  .brand__mark {
    flex: none;
    width: 18px; height: 18px; border-radius: 50%;
    background: var(--orange-light);
  }
  .brand__name {
    font-weight: 800;
    font-size: 30px;
    letter-spacing: 1.5px;
    color: var(--brand-green);
    line-height: 1;
  }
  .page--front .brand { left: 35px; top: 160px; }
  .page--back .brand {
    left: 0; top: 712px; width: 193px;
    justify-content: center;
    gap: 6px;
  }
  .page--back .brand__mark { width: 13px; height: 13px; }
  .page--back .brand__name { font-size: 24px; letter-spacing: 1px; }

  .intro {
    position: absolute; left: 35px; top: 212px; width: 170px;
    font-size: 9.6px; line-height: 13.5px;
  }

  .section { position: absolute; }
  .section__title {
    color: var(--accent);
    font-weight: 500;
    font-size: 17px;
    line-height: 1;
    margin-bottom: 13px;
  }
  .section p {
    font-size: 11.4px;
    line-height: 14.5px;
    margin-bottom: 13px;
  }
  .section--general { left: 35px; top: 352px; width: 272px; }
  .section--concussion { left: 352px; top: 501px; width: 205px; }

  .photo-column {
    position: absolute; left: 0; top: 0; width: 193px; height: 554px;
    background: linear-gradient(180deg, #bdbdbd 0%, #d9d9d9 55%, #ffffff 100%);
  }
  .services {
    position: absolute; left: 193px; top: 0; width: 374px; height: 802px;
    background: var(--mint);
  }
  .services .section { position: static; margin: 0 0 0 19px; width: 335px; }
  .services .section__title { font-size: 16px; margin-bottom: 14px; }
  .services .section p { font-size: 10.6px; line-height: 13.4px; margin-bottom: 0; }
  .services .section + .section { margin-top: 22px; }
  .services__list { position: absolute; left: 0; top: 48px; }
</style>
</head>
<body>

<section class="page page--front">
  <svg class="wave-art" viewBox="0 0 580 820">
    <defs>
      <linearGradient id="ribbon" x1="0" y1="0" x2="0.4" y2="1">
        <stop offset="0" stop-color="#e8670f"/>
        <stop offset="0.45" stop-color="#ec780d"/>
        <stop offset="1" stop-color="#f3960a"/>
      </linearGradient>
      <linearGradient id="clinician" x1="0" y1="0" x2="1" y2="1">
        <stop offset="0" stop-color="#e4e9ee"/>
        <stop offset="0.55" stop-color="#c9d3dc"/>
        <stop offset="1" stop-color="#3e6fb8"/>
      </linearGradient>
    </defs>
    <path role="img" aria-label="Photo of a clinician in blue scrubs and surgical cap"
          d="M374,0 C370,80 360,200 362,290 C420,300 500,310 580,334 L580,0 Z"
          fill="url(#clinician)"/>
    <path d="M282,0 C255,110 260,230 330,300 C400,370 500,400 580,486 L580,334 C500,310 420,300 362,290 C360,200 370,80 374,0 Z"
          fill="url(#ribbon)"/>
  </svg>

  <div class="brand">
    <span class="brand__mark"></span>
    <span class="brand__name">KINETRA</span>
  </div>
  <p class="intro">orem ipsum dolor sit amet, consectetur adipiscing elit, sed do eius</p>

  <article class="section section--general">
    <h2 class="section__title">General clinic</h2>
    <p>sit amet, consectetur adipiscing elit, sed do eiusmod tempor incididunt ut labore et dolore magna aliqua. Ut enim ad minim veniam, quis nostrud exercitation ullamco laboris nisi ut aliquip ex ea commodo consequat. Duis aute irure dolor in reprehenderit in voluptate velit esse cillum dolore eu fugiat nulla pariatur.<br>Excepteur sint occaecat cupidatat non proident, sunt in culpa qui officia deserunt mollit anim id est laborum."</p>
    <p>sit amet, consectetur adipiscing elit, sed do eiusmod tempor incididunt ut labore et dolore magna aliqua. Ut enim ad minim veniam, quis nostrud exercitation ullamco laboris nisi ut aliquip ex ea commodo consequat. Duis aute irure dolor in reprehenderit in voluptate velit esse cillum dolore eu fugiat nulla pari.<br>Excepteur sint occaecat cupidatat non proident, sunt in culpa qui officia serunt mollit anim id est laborum."</p>
    <p>do eiusmod tempor incididunt ut labore et dolore magna aliqua. Ut enim ad minim veniam, quis nostrud exercitation ullamco laboris nisi ut aliquip ex ea commodo consequat. esse cillum dolore eu fugiat nulla pariatur.</p>
  </article>

  <article class="section section--concussion">
    <h2 class="section__title">Concussion</h2>
    <p>orem ipsum dolor sit amet, consectetur adipiscing elit, sed do eiusmod tempor incididunt ut labore et dolore magna aliqua. Ut enim ad minim veniam, quis nostrud exercitation ullamco laboris nisi ut aliquip ex ea commodo consequat. Duis aute irure dolor in reprehenderit in voluptate velit esse cillum dolore eu fugiat nulla pariatur. Excepteur sint occaecat cupidatat non proident, sunt in culpa qui officia deserunt mollit anim id est laborum."</p>
    <p>velit esse cillum dolore eu fugiat nulla pariatur. Excepteur sint occaecat cupidatat non proident, sunt in culpa fugiat nulla pariatur.</p>
  </article>
</section>

<section class="page page--back">
  <div class="photo-column" role="img" aria-label="Soft-focus black and white photo of a doctor's coat and stethoscope"></div>

  <div class="brand">
    <span class="brand__mark"></span>
    <span class="brand__name">KINETRA</span>
  </div>

  <div class="services">
    <div class="services__list">
      <article class="section">
        <h2 class="section__title">Podiatry</h2>
        <p>sit amet, consectetur adipiscing elit, sed do eiusmod tempor incididunt ut labore et dolore magna aliqua. Ut enim ad minim veniam, quis nostrud exercitation ullamco laboris nisi ut aliquip ex ea commodo consequat. Duis aute irure dolor in reprehenderit in voluptate velit esse cillum dolore eu fugiat nulla pariatur. Excepteur sint occaecat cupidatat non proident, sunt in culpa qui officia deserunt mollit anim id est laborum."</p>
      </article>
      <article class="section">
        <h2 class="section__title">Sports Physicians</h2>
        <p>sit amet, consectetur adipiscing elit, sed do eiusmod tempor incididunt ut labore et dolore magna aliqua. Ut enim ad minim veniam, quis nostrud exercitation ullamco laboris nisi ut aliquip ex ea commodo consequat. Duis aute irure dolor in reprehenderit in voluptate velit esse cillum dolore eu fugiat nulla pariatur. Excepteur sint occaecat cupidatat non proident, sunt in culpa qui officia deserunt mollit anim id est laborum."</p>
      </article>
      <article class="section">
        <h2 class="section__title">Exercise Physiology</h2>
        <p>sit amet, consectetur adipiscing elit, sed do eiusmod tempor incididunt ut labore et dolore magna aliqua. Ut enim ad minim veniam, quis nostrud exercitation ullamco laboris nisi ut aliquip ex ea commodo consequat. Duis aute irure dolor in reprehenderit in voluptate velit esse cillum dolore eu fugiat nulla pariatur. Excepteur sint occaecat cupidatat non proident, sunt in culpa qui officia deserunt mollit anim id est laborum."</p>
      </article>
      <article class="section">
        <h2 class="section__title">Osteoarthritis</h2>
        <p>sit amet, consectetur adipiscing elit, sed do eiusmod tempor incididunt ut labore et dolore magna aliqua. Ut enim ad minim veniam, quis nostrud exercitation ullamco laboris nisi ut aliquip ex ea commodo consequat. Duis aute irure dolor in reprehenderit in voluptate velit esse cillum dolore eu fugiat nulla pariatur. Excepteur sint occaecat cupidatat non proident, sunt in culpa qui officia deserunt mollit anim id est laborum."</p>
      </article>
      <article class="section">
        <h2 class="section__title">Physiotherapy</h2>
        <p>sit amet, consectetur adipiscing elit, sed do eiusmod tempor incididunt ut labore et dolore magna aliqua. Ut enim ad minim veniam, quis nostrud exercitation ullamco laboris nisi ut aliquip ex ea commodo consequat. Duis aute irure dolor in reprehenderit in voluptate velit esse cillum dolore eu fugiat nulla pariatur. Excepteur sint occaecat cupidatat non proident, sunt in culpa qui officia deserunt mollit anim id est laborum."</p>
      </article>
    </div>
  </div>
</section>

</body>
</html>
```